Podcast Graphics For Internet Business Building Podcast

We need new podcast graphics.
1400x1400
300dpi

Needs to include text "Quiet Harbor Ledger Hour" as the podcast title and "Creative Internet Income Strategies" as a subtitle.

We like blue and grey as our main colors, but are open to other schemes.

Please see attached image for an example of podcast graphics we like. While we prefer a more plain look, it would be nice to have a subtle hint related to a "machine" in the background. Something like a pencil sketch of cogs like on the Quiet Harbor Ledger 10 book cover (attached image).

Target Market(s)

online entrepreneurs or those who want to start an online business

Font styles to use
Sans Serif

Colors
0455a3
3277b5

Requirements
Must have
• Text noted in project description
Should not have
• No money symbols or flashy "make money" type things.

```html
<!DOCTYPE html>
<html lang="en">
<head>
<meta charset="utf-8">
<title>Quiet Harbor Ledger Hour – Podcast Cover</title>
<link rel="stylesheet" href="https://fonts.googleapis.com/css2?family=Mulish:wght@400;600&display=swap">
<style>
  :root {
    --violet-deep: #3a26d9;
    --violet-bright: #9b4ef2;
    --blue-soft: #6f86ec;
    --blue-mid: #4a3fe3;
    --text-light: #ffffff;
  }
  html, body {
    margin: 0;
    padding: 0;
    width: 1200px;
    height: 1200px;
    overflow: hidden;
    background: var(--violet-deep);
  }
  .cover {
    position: relative;
    width: 1200px;
    height: 1200px;
    overflow: hidden;
    font-family: "Mulish", sans-serif;
    color: var(--text-light);
  }
  .cover__backdrop {
    position: absolute;
    inset: 0;
    background:
      radial-gradient(circle at 100% 0%, var(--blue-soft) 0%, rgba(111,134,236,0) 55%),
      radial-gradient(circle at 0% 100%, var(--violet-bright) 0%, rgba(155,78,242,0) 60%),
      linear-gradient(135deg, var(--blue-mid) 0%, var(--violet-deep) 50%, #5a3ae6 100%);
  }
  .cover__title {
    position: absolute;
    left: 94px;
    top: 87px;
    margin: 0;
    font-weight: 400;
    font-size: 153px;
    line-height: 170px;
    letter-spacing: -1px;
  }
  .cover__title span {
    display: block;
    white-space: nowrap;
  }
  .cover__subtitle {
    position: absolute;
    left: 95px;
    top: 1051px;
    margin: 0;
    font-weight: 600;
    font-size: 44px;
    line-height: 1;
    letter-spacing: 3.2px;
    text-transform: uppercase;
    white-space: nowrap;
  }
</style>
</head>
<body>
  <main class="cover">
    <div class="cover__backdrop" role="img" aria-label="Overhead photo of a wooden business desk with laptop, coffee cup, invoice clipboard, newspaper, calculator and calendar, tinted in a blue-violet gradient"></div>
    <h1 class="cover__title">
      <span>Quiet</span>
      <span>Harbor</span>
      <span>Ledger</span>
      <span>Hour</span>
    </h1>
    <p class="cover__subtitle">Creative Internet Income Strategies</p>
  </main>
</body>
</html>
```